Ironfinch Steakhouse

We are changing our restaurant from a casual upmarket dining restaurant, to an upmarket steakhouse. The restaurant is located at Ironfinch Lodge, Silver Pike Alpine Resort, BC, Canada.

The A - frame Signs are 3 feet wide by 5 foot high.
Must also work as a poster size.

Target Market(s)

25 to 65's skiers, families, affluent home owners.

Industry/Entity Type

Restaurant

Colors

Designer to choose colors to be used in the design.

Requirements
Must have
• A big, juicy, flame grilled steak image.
• Located at Ironfinch lodge.
Nice to have
• Must be bold and enticing, need to convince the tired skiers that they just have to have an awesome steak for dinner.
• Should be simple, straight to the point.
• People drinking, dining, having a great dining experience.
Should not have
• bright colors

```html
<!DOCTYPE html>
<html lang="en">
<head>
<meta charset="utf-8">
<title>Ironfinch Steakhouse</title>
<link href="https://fonts.googleapis.com/css2?family=Cinzel:wght@400;500;600&display=swap" rel="stylesheet">
<style>
  :root {
    --night: #000000;
    --ivory: #ffffff;
    --ember: #e8761a;
    --flame: #ffc247;
    --glow: #ffe08a;
    --char: #2a1208;
    --sear: #7c3514;
    --crust: #a44f22;
  }
  html, body {
    margin: 0;
    padding: 0;
    width: 721px;
    height: 1200px;
    overflow: hidden;
    background: var(--night);
  }
  .sign {
    position: relative;
    width: 721px;
    height: 1200px;
    background: var(--night);
    color: var(--ivory);
    font-family: "Cinzel", "Trajan Pro", serif;
    overflow: hidden;
  }
  .brand-mark {
    position: absolute;
    left: 0;
    top: 128px;
    width: 100%;
    display: flex;
    justify-content: center;
    align-items: center;
    gap: 18px;
  }
  .brand-mark-dot {
    width: 40px;
    height: 40px;
    border-radius: 50%;
    background: var(--ivory);
  }
  .brand-mark-name {
    font-size: 46px;
    font-weight: 400;
    letter-spacing: 4px;
    line-height: 1;
    text-transform: uppercase;
  }
  .brand-rule {
    position: absolute;
    left: 54px;
    top: 239px;
    width: 613px;
    height: 1.5px;
    background: var(--ivory);
  }
  .brand-name {
    position: absolute;
    left: 0;
    top: 248px;
    width: 100%;
    margin: 0;
    text-align: center;
    font-weight: 400;
    text-transform: uppercase;
    line-height: 84px;
  }
  .brand-name span {
    display: block;
    font-size: 72px;
    letter-spacing: 3px;
  }
  .brand-name span::first-letter {
    font-size: 92px;
  }
  .grill-photo {
    position: absolute;
    left: 0;
    top: 478px;
    width: 721px;
    height: 546px;
    background:
      radial-gradient(ellipse 30% 20% at 25% 38%, var(--crust) 0%, var(--sear) 45%, rgba(124,53,20,0) 100%),
      radial-gradient(ellipse 28% 20% at 78% 30%, var(--crust) 0%, var(--sear) 45%, rgba(124,53,20,0) 100%),
      radial-gradient(ellipse 30% 24% at 50% 66%, var(--crust) 0%, var(--sear) 50%, rgba(124,53,20,0) 100%),
      radial-gradient(ellipse 22% 18% at 85% 78%, var(--glow) 0%, var(--flame) 40%, rgba(255,194,71,0) 100%),
      radial-gradient(ellipse 16% 14% at 48% 42%, var(--flame) 0%, rgba(255,194,71,0) 100%),
      radial-gradient(ellipse 22% 16% at 22% 60%, var(--ember) 0%, rgba(232,118,26,0) 100%),
      radial-gradient(ellipse 70% 45% at 55% 85%, var(--ember) 0%, var(--char) 60%, rgba(42,18,8,0) 100%),
      linear-gradient(180deg, var(--night) 0%, var(--char) 22%, #3c1a0a 60%, var(--char) 94%, var(--night) 100%);
  }
  .location {
    position: absolute;
    left: 0;
    top: 1072px;
    width: 100%;
    text-align: center;
    text-transform: uppercase;
    font-weight: 500;
    margin: 0;
  }
  .location-lead {
    display: block;
    font-size: 34px;
    line-height: 46px;
    letter-spacing: 1px;
  }
  .location-venue {
    display: block;
    font-size: 40px;
    line-height: 54px;
    letter-spacing: 1.5px;
  }
</style>
</head>
<body>
  <main class="sign">
    <div class="brand-mark">
      <span class="brand-mark-dot" aria-hidden="true"></span>
      <span class="brand-mark-name">Ironfinch</span>
    </div>
    <div class="brand-rule"></div>
    <h1 class="brand-name">
      <span>Ironfinch</span>
      <span>Steakhouse</span>
    </h1>
    <div class="grill-photo" role="img" aria-label="Three seasoned steaks searing on a round charcoal grill over bright flames"></div>
    <p class="location">
      <span class="location-lead">Located at</span>
      <span class="location-venue">Ironfinch Lodge</span>
    </p>
  </main>
</body>
</html>
```